Wordpress Lifestyle Blog

Just to be clear - I have the domain and the wordpress site (which is messy). I need someone to help me complete a simple blog design and then go into the existing wordpress site, and get rid of all the existing rubbish and set up the templates please. If we progress with design can we please be clear about additional costs upfront which, of course, I appreciate is the case.

Need a lifestyle blog. It is called brightyearsahead.com. Aimed at the older woman but needs to look fresh and young, not old fashioned. Navigation will be Home, Fashion, Feelings, Fitness, Contact. I have a logo but not sure it will work at the moment so happy with stylised words.Will have social media links.

Need homepage (not overly long) to have a main slider for pics/videos. Then the three category boxes underneath linking through to 2nd level pages containing blogs for that category and then the actual blog page. Happy to be led by expertise if this is not gonna work.

Am really looking for something clean and fresh like a Marwyn type approach to be honest.

If you need any further direction please just ask - once design chosen I am looking to move quickly.

Thank you so much for looking at this brief

Target Market(s)

Women, 40 - 60 age group but with a younger outlook

Number of Pages Required

3 page

Colors

Designer to choose colors to be used in the design.

Requirements
Must have
• Reflect youth, fun, bright
• Lift easily into a wordpress format
Should not have
• Old, staid, frumpy,dark

```html
<!DOCTYPE html>
<html lang="en">
<head>
<meta charset="utf-8">
<title>Fashion — brightyearsahead.com</title>
<link href="https://fonts.googleapis.com/css2?family=Spectral:wght@300;400&family=Crimson+Text:wght@400;600&display=swap" rel="stylesheet">
<style>
:root{
  --ink:#1e1e1e;
  --muted:#9a9a9a;
  --pink:#f2c4c6;
  --pink-text:#e7a3a7;
  --rule:#e8e8e8;
  --white:#ffffff;
  --logo-blue:#9fd3ec;
}
*{box-sizing:border-box;margin:0;padding:0}
html,body{width:1200px;height:2429px;overflow:hidden;background:var(--white)}
body{position:relative;font-family:"Crimson Text",Georgia,serif;color:var(--ink)}
.site-logo{position:absolute;top:58px;left:0;width:1200px;text-align:center;font-family:"Spectral",Georgia,serif;font-weight:300;font-size:58px;letter-spacing:1px;color:var(--logo-blue)}
.header-rule{position:absolute;top:172px;left:168px;width:868px;border-top:1px solid var(--rule)}
.main-nav{position:absolute;top:188px;left:0;width:1200px;display:flex;justify-content:center;align-items:center;gap:22px;font-size:12px;letter-spacing:.4px;text-transform:uppercase}
.main-nav .active{color:var(--pink-text)}
.page-title{position:absolute;top:246px;left:0;width:1200px;text-align:center;font-family:"Spectral",Georgia,serif;font-weight:400;font-size:50px}
.filters{position:absolute;top:350px;left:0;width:1200px;display:flex;justify-content:center;gap:5px}
.filters span{height:27px;padding:0 12px;display:flex;align-items:center;background:var(--pink);color:var(--white);font-size:9px;letter-spacing:.6px;text-transform:uppercase}
.filters .current{background:var(--white);border:1px solid var(--pink);color:var(--pink-text)}
.post{position:absolute;width:420px;text-align:center}
.post-image{width:100%}
.post-cats{margin-top:20px;font-size:11px;letter-spacing:.3px;text-transform:uppercase}
.post-cats i{text-transform:none;font-size:12px}
.post-title{margin-top:22px;font-family:"Spectral",Georgia,serif;font-weight:400;font-size:30px;line-height:32px;text-transform:uppercase}
.post-byline{margin-top:8px;font-size:13px;color:var(--muted)}
.post-byline b{font-weight:400;color:var(--ink)}
.post-date{font-size:13px;color:var(--muted);line-height:18px}
.post-excerpt{margin-top:18px;text-align:justify;font-size:15px;line-height:19.5px}
.post-excerpt p+p{margin-top:28px;text-align:center}
.dropcap{float:left;font-family:"Spectral",Georgia,serif;font-size:62px;line-height:62px;padding:8px 12px 8px 0;margin:4px 12px 0 24px;border-right:1px solid var(--ink)}
.view-post{display:inline-block;margin-top:28px;height:30px;padding:0 22px;line-height:30px;background:var(--pink);color:var(--white);font-size:9px;letter-spacing:1px;text-transform:uppercase}
.social-links{position:absolute;top:1912px;left:0;width:1200px;display:flex;justify-content:center;gap:14px;font-size:8px;text-transform:uppercase;letter-spacing:.3px;color:#555}
.social-links span::before{content:"";display:inline-block;width:6px;height:6px;border-radius:50%;background:#777;margin-right:3px;vertical-align:middle}
.feed-title{position:absolute;top:1942px;left:0;width:1200px;text-align:center;font-size:20px}
.feed-grid{position:absolute;top:1972px;left:0;width:1200px;display:grid;grid-template-columns:repeat(6,200px);grid-auto-rows:200px}
.feed-grid div{position:relative}
.feed-caption{position:absolute;inset:0;display:flex;flex-direction:column;justify-content:center;align-items:center;color:var(--white);font-size:10px;gap:4px}
.site-footer{position:absolute;top:2404px;left:288px;width:640px;display:flex;justify-content:space-between;font-size:8px;color:#444}
.site-footer .back{text-transform:uppercase}
</style>
</head>
<body>
<div class="site-logo">bright years ahead</div>
<div class="header-rule"></div>
<nav class="main-nav">
  <span>Home</span><span class="active">Fashion</span><span>Feelings</span><span>Fitness</span><span>Contact</span>
  <svg width="13" height="13" viewBox="0 0 13 13" aria-label="Search"><circle cx="5.5" cy="5.5" r="4" fill="none" stroke="#1e1e1e" stroke-width="2"/><line x1="8.5" y1="8.5" x2="12" y2="12" stroke="#1e1e1e" stroke-width="2"/></svg>
</nav>
<h1 class="page-title">FASHION</h1>
<div class="filters"><span class="current">Fashion</span><span>Feelings</span><span>Fitness</span></div>

<article class="post" style="left:168px;top:403px">
  <div class="post-image" style="height:251px;background:linear-gradient(180deg,#7fb6de 0%,#b9d6ea 45%,#cfcac4 70%,#e0ddd8 100%)" role="img" aria-label="Dancer leaping beneath a concrete bridge"></div>
  <div class="post-cats"><i>in</i>Fashion, Feelings, Fitness</div>
  <h2 class="post-title">Slideshow Post Type Gallery</h2>
  <div class="post-byline">by <b>Clara Bennett</b></div>
  <div class="post-date">Saturday, August 8, 2015</div>
  <div class="post-excerpt">
    <p><span class="dropcap">H</span>ollis Barrow striking a pose with a hoard of puppies! Gideon-Kai Dalrymple breaking into song! Hana Vell slinking about in a décolletage-diving blazer! Welcome to a Fashion Week model casting—Maisonmode.com style.</p>
    <p>And it wasn't just a typical waiting-around-for-fittings affair, either. Instead, call it the ultimate playground of all casting calls, starting from the outside, where Pim Orr lensed the grand entrances of the insouciant-cool models-off-duty en masse, while photographer Sofia Marlowe created editorial-worthy portraits of several of the stunners on the sidewalks.</p>
  </div>
  <span class="view-post">View post</span>
</article>

<article class="post" style="left:612px;top:403px">
  <div class="post-image" style="height:251px;background:linear-gradient(180deg,#f1f1f0 0%,#e4e3e1 60%,#a08a7a 100%)" role="img" aria-label="Bright white interior with a black sling chair"></div>
  <div class="post-cats"><i>in</i>Fashion, Feelings</div>
  <h2 class="post-title">Look of the Day</h2>
  <div class="post-byline">by <b>Clara Bennett</b></div>
  <div class="post-date">Saturday, July 4, 2015</div>
  <div class="post-excerpt">
    <p><span class="dropcap">S</span>ed ut perspiciatis unde omnis iste natus error sit voluptatem accusantium doloremque laudantium, totam rem aperiam, eaque ipsa quae ab illo inventore veritatis et quasi architecto beatae vitae dicta sunt explicabo. Nemo enim ipsam voluptatem quia voluptas sit aspernatur aut odit aut fugit, sed quia consequuntur magni dolores eos qui ratione voluptatem sequi nesciunt.</p>
  </div>
  <span class="view-post">View post</span>
</article>

<article class="post" style="left:168px;top:1164px">
  <div class="post-image" style="height:285px;background:linear-gradient(90deg,#f4f4f4 0%,#3a4a7a 45%,#f4f4f4 55%,#d8d8d8 100%)" role="img" aria-label="Two portraits of a model in a dark suit"></div>
  <div class="post-cats"><i>in</i>Fashion, Fitness</div>
  <h2 class="post-title">Four of the Best Secret Shopping Destinations in Milan</h2>
  <div class="post-byline">by <b>Clara Bennett</b></div>
  <div class="post-date">Monday, November 24, 2014</div>
  <div class="post-excerpt">
    <p><span class="dropcap">S</span>ometimes ignorance is leverage. A few years back, when I made the switch from one media company to another, it was precisely the lack of transparency about my salary that allowed me to more than double my salary in the process.</p>
  </div>
  <span class="view-post">View post</span>
</article>

<article class="post" style="left:611px;top:1039px;width:423px">
  <div class="post-image" style="height:334px;background:linear-gradient(135deg,#f0bcc0 0%,#f3c6c8 40%,#a6dcea 60%,#9fd6e6 100%)" role="img" aria-label="Clear glasses on a pink and blue background"></div>
  <div class="post-cats" style="margin-top:44px"><i>in</i>Fashion, Feelings</div>
  <h2 class="post-title">Daley Spent – Self Hosted Audio Post</h2>
  <div class="post-byline">by <b>Clara Bennett</b></div>
  <div class="post-date">Saturday, July 4, 2015</div>
  <div class="post-excerpt">
    <p><span class="dropcap">P</span>ellentesque habitant morbi tristique senectus et netus et malesuada fames ac turpis egestas. Vestibulum tortor quam, feugiat vitaePellentesque habitant morbi tristique senectus et netus et malesuada fames ac turpis egestas.</p>
  </div>
  <span class="view-post">View post</span>
</article>

<div class="social-links"><span>Like on Facelink</span><span>Follow on Chirper</span><span>Follow on Snapgram</span><span>Gossip on Blogfolio</span></div>
<div class="feed-title">Snapgram</div>
<div class="feed-grid">
  <div style="background:linear-gradient(#d9d2ca,#3b3533)" role="img" aria-label="Outfit photo in a black playsuit"></div>
  <div style="background:linear-gradient(#cfc7bb,#e8c46a)" role="img" aria-label="Outfit photo in a yellow ruffle top"></div>
  <div style="background:linear-gradient(#e8dfdb,#e9b3a6)" role="img" aria-label="Outfit photo in a gingham set"></div>
  <div style="background:linear-gradient(#8a8d93,#ece8e2)" role="img" aria-label="Outfit photo in a white lace dress"></div>
  <div style="background:linear-gradient(#e6e2da,#c9c9b0)" role="img" aria-label="Outfit photo in a white skirt"></div>
  <div style="background:linear-gradient(#cfa58f,#2c2424)" role="img" aria-label="Outfit photo in a black top"></div>
  <div style="background:linear-gradient(#c9b7a3,#e5b560)" role="img" aria-label="Outfit photo in a floral dress"></div>
  <div style="background:linear-gradient(#8f9a9a,#dde3e2)" role="img" aria-label="Outfit photo in a check top"></div>
  <div style="background:linear-gradient(#eeeeee,#5d6660)" role="img" aria-label="Outfit photo on white steps"></div>
  <div style="background:#2e2e30" role="img" aria-label="Outfit photo in a corset top"><div class="feed-caption"><span>♡ 6834 &nbsp; ◯ 28</span><span>Rosalie Corset Top ...</span></div></div>
  <div style="background:linear-gradient(#d6cfc5,#403835)" role="img" aria-label="Mirror photo in a black dress"></div>
  <div style="background:linear-gradient(#ddd5cc,#e8a38f)" role="img" aria-label="Outfit photo in a pink check dress"></div>
</div>
<footer class="site-footer"><span>Copyright ©</span><span class="back">Back to top</span></footer>
</body>
</html>
```